Plover Freightworks Business Card Design

We are a trucking and warehousing company. We run freight in the US manly from the Pacific NW to TX and back up the the PNW. We also do warehousing where we store, move, and distribute freight. Looking for a clean and modern design of business card. We would like to look rich and elegant. Attached is our logo.

Industry/Entity Type

Trucking Company

Contact Information for Business Card

Looking for a clean and modern design of business card. We would like to look rich and elegant.

Font styles to use
Sans Serif

Colors

Designer to choose colors to be used in the design.

Requirements
Must have
• logo but it should not dominate the card
Should not have
• logo should not dominate the card

```html
<!DOCTYPE html>
<html lang="en">
<head>
<meta charset="utf-8">
<title>Plover Freightworks Business Card</title>
<link href="https://fonts.googleapis.com/css2?family=Roboto:wght@400;500;700&display=swap" rel="stylesheet">
<style>
  :root{
    --bg:#e4e4e4;
    --paper:#ffffff;
    --blue:#1d5fa8;
    --orange:#e58a1c;
    --dark:#2e2321;
    --ink:#3a3a3a;
  }
  *{box-sizing:border-box;margin:0;padding:0}
  html,body{width:1200px;height:852px;overflow:hidden}
  body{background:var(--bg);font-family:"Roboto",Arial,sans-serif;position:relative}
  .card{position:absolute;top:278px;width:520px;height:297px;background:var(--paper);border-radius:18px;overflow:hidden;box-shadow:0 4px 14px rgba(0,0,0,.12)}
  .card--front{left:50px}
  .card--back{left:630px}

  /* front */
  .brand{display:flex;align-items:center;gap:14px}
  .brand__mark{width:44px;height:44px;border-radius:50%;background:var(--blue);flex:none}
  .brand__name{font-weight:700;color:var(--dark);line-height:1.05;letter-spacing:.5px}
  .card--front .brand{position:absolute;left:0;right:0;top:86px;justify-content:center}
  .card--front .brand__name{font-size:34px}
  .card--front .brand__name small{display:block;font-size:20px;font-weight:700;letter-spacing:2px}
  .front__web{position:absolute;left:0;right:0;top:190px;text-align:center;font-size:14px;color:var(--ink)}
  .front__rule{position:absolute;left:0;top:0}

  /* back */
  .card--back .brand{position:absolute;left:30px;top:104px;align-items:flex-start}
  .card--back .brand__name{font-size:26px}
  .card--back .brand__name small{display:block;font-size:16px;font-weight:700;letter-spacing:1.5px;margin-top:4px}
  .back__wave{position:absolute;left:0;top:0}
  .holder{position:absolute;right:26px;top:24px;text-align:right;color:var(--ink)}
  .holder__name{font-size:21px;font-weight:700;color:var(--blue)}
  .holder__title{font-size:12px;margin-top:2px}
  .holder__address{font-size:12px;margin-top:8px;line-height:1.4}
  .contacts{position:absolute;right:22px;top:168px;list-style:none;color:#fff;font-size:13px;text-align:right}
  .contacts li{display:flex;justify-content:flex-end;align-items:center;gap:8px;height:19px}
  .contacts svg{width:11px;height:11px;flex:none}
</style>
</head>
<body>

<section class="card card--front" aria-label="Card front">
  <svg class="front__rule" width="520" height="297" viewBox="0 0 520 297" aria-hidden="true">
    <line x1="290" y1="72" x2="395" y2="72" stroke="var(--blue)" stroke-width="3"/>
    <rect x="395" y="70" width="125" height="5" fill="var(--dark)"/>
    <line x1="110" y1="222" x2="220" y2="222" stroke="var(--blue)" stroke-width="3"/>
    <rect x="220" y="219" width="125" height="6" fill="var(--orange)"/>
    <rect x="345" y="219" width="175" height="6" fill="var(--dark)"/>
    <rect x="0" y="287" width="260" height="10" fill="var(--blue)"/>
    <rect x="260" y="287" width="260" height="10" fill="var(--dark)"/>
  </svg>
  <div class="brand">
    <span class="brand__mark"></span>
    <span class="brand__name">Plover Freightworks<small>LLC</small></span>
  </div>
  <p class="front__web">www.ploverfreightworks.com</p>
</section>

<section class="card card--back" aria-label="Card back">
  <svg class="back__wave" width="520" height="297" viewBox="0 0 520 297" aria-hidden="true">
    <path d="M0,272 C140,272 240,252 295,192 C340,150 410,140 520,142 L520,297 L0,297 Z" fill="var(--blue)"/>
    <path d="M120,254 C215,242 255,214 292,172 C336,130 410,124 520,126" fill="none" stroke="var(--dark)" stroke-width="5"/>
    <path d="M0,260 C120,260 205,242 268,202 C220,252 130,268 0,271 Z" fill="var(--orange)"/>
  </svg>
  <div class="holder">
    <p class="holder__name">Daniel Marsh</p>
    <p class="holder__title">Managing Director</p>
    <p class="holder__address">2740 Harbor Lane, Fort<br>Lyle, OR 97201</p>
  </div>
  <div class="brand">
    <span class="brand__mark"></span>
    <span class="brand__name">Plover<br>Freightworks<small>LLC</small></span>
  </div>
  <ul class="contacts">
    <li>555 0142 388
      <svg viewBox="0 0 12 12" aria-hidden="true"><path d="M2 1h3l1 3-2 1c1 2 2 3 4 4l1-2 3 1v3c-6 0-10-4-10-10z" fill="#fff"/></svg>
    </li>
    <li>ploverfreightworks.com
      <svg viewBox="0 0 12 12" aria-hidden="true"><circle cx="6" cy="6" r="5" fill="none" stroke="#fff" stroke-width="1.2"/><ellipse cx="6" cy="6" rx="2.2" ry="5" fill="none" stroke="#fff" stroke-width="1"/><line x1="1" y1="6" x2="11" y2="6" stroke="#fff" stroke-width="1"/></svg>
    </li>
    <li>daniel@ploverfreightworks.com
      <svg viewBox="0 0 12 12" aria-hidden="true"><rect x="0.5" y="2.5" width="11" height="7" fill="#fff"/><path d="M0.5 2.5 6 7 11.5 2.5" fill="none" stroke="var(--blue)" stroke-width="1"/></svg>
    </li>
  </ul>
</section>

</body>
</html>
```